Complete Stationary Package Needed for New Dental Office ! ! !

I'm moving my dental office and would like to use my existing logo to create a new:
- Business Card (please submit Business Card designs to this project - http://work.pitchvault.net/brief.aspx?id=514296)
- Appointment Card (submit here)
- Letterhead (submit here)
- Envelope (submit here)
My practice name (within my logo) is:
Morris T. Lindqvist, D.D.S., P.A.
Family and Cosmetic Dentistry
***Obviously you will notice that the lower leg of the "K" in my logo is a smile.
My new address and contact information is:
372 Hollisbrook Lane, Suite 118
Cary, NC 27634
919-472-3081 (ph)
919-472-3095 (fax)
info@lindqvistdds.example
www.lindqvistdds.example
If you would like to use a tagline, I would suggest "Precision Dentistry with a Personal Touch".
I have attached my logo in numerous formats.
I have also attached 2 QR codes, one of which links to my website and the other one which links to a "Like" page for my business Chatterbook page. These QR codes could be improved by putting a graphic in the middle, but I created these myself and did not know how to do this.
Thank you for your time. I look forward to seeing all of your creative ideas!
Depending on the designs, I may award 2 different winners for the Business Card project and the Stationery Project. Or if a design is really good, I will award both projects to the same designer.
Updates
Project Deadline Extended
Reason: PitchVault administrators recently helped me split my project into 2 projects - 1 for business card and 1 for letterhead, envelope, etc. and I would like sufficient time to receive designs and provide feedback. Thank you.
Target Market(s)
Current and prospective dental patients.
Industry/Entity Type
Dental
Requirements
Must have
- Please ensure business card has a 2-sided design.
- Please ensure that your design is "practical" for printing purposes.
Nice to have
- Improvement of QR codes by addition of graphics in the middle to differentiate them. Incorporation of QR codes into business card design, maybe on the back side? I would consider the Chatterbook QR code more important than the website QR code simply because my website URL is very easy to type.
Should not have
- Please, NO "floating" or "extracted" teeth which sends an undesirable message.

```html
<!DOCTYPE html>
<html lang="en">
<head>
<meta charset="utf-8">
<title>Letterhead – Morris T. Lindqvist, D.D.S., P.A.</title>
<link rel="stylesheet" href="https://fonts.googleapis.com/css2?family=Sorts+Mill+Goudy&display=swap">
<style>
  :root{
    --backdrop:#e3eaed;
    --paper:#ffffff;
    --navy:#1f1c4e;
    --teal:#00625e;
    --teal-dark:#004d4a;
    --rule:#3a3a3a;
    --wave-light:#e6e8e8;
    --ghost:#efefef;
  }
  *{box-sizing:border-box;margin:0;padding:0}
  html,body{width:1200px;height:900px;overflow:hidden;background:var(--backdrop)}
  body{font-family:"Sorts Mill Goudy",Georgia,serif;display:flex;align-items:center;justify-content:center}
  .letterhead{position:relative;width:600px;height:848px;background:var(--paper);box-shadow:0 4px 14px rgba(0,0,0,.12);overflow:hidden}
  .letterhead__header{position:absolute;left:36px;right:36px;top:34px;height:103px;border-bottom:1px solid var(--rule);display:flex;justify-content:space-between}
  .brand{display:flex;gap:12px}
  .brand__mark{width:75px;height:75px;background:var(--teal);flex:none}
  .brand__text{padding-top:4px}
  .brand__name{font-size:17px;color:var(--navy);font-variant:small-caps;letter-spacing:.3px;line-height:1;border-bottom:1px solid var(--navy);padding-bottom:2px;margin-left:-22px;padding-left:0}
  .brand__tagline{font-size:11px;color:var(--teal);font-variant:small-caps;letter-spacing:.8px;margin-top:2px}
  .brand__address{font-size:12px;color:var(--teal-dark);line-height:18px;margin-top:6px}
  .contact{list-style:none;padding-top:14px;text-align:right}
  .contact__item{font-size:12px;color:var(--teal-dark);display:flex;align-items:center;justify-content:flex-end;gap:9px;height:21.5px}
  .contact__icon{width:14px;height:14px;flex:none}
  .watermark{position:absolute;left:0;right:0;top:470px;text-align:center;font-size:110px;color:var(--ghost);line-height:1}
  .letterhead__footer{position:absolute;left:0;bottom:0;width:600px;height:100px}
  .footer__motto{position:absolute;left:0;right:0;bottom:9px;text-align:center;color:#fff;font-size:12px}
</style>
</head>
<body>
<main class="letterhead">
  <header class="letterhead__header">
    <div class="brand">
      <div class="brand__mark" aria-hidden="true"></div>
      <div class="brand__text">
        <h1 class="brand__name" style="margin-left:0">Morris T. Lindqvist, D.D.S., P.A.</h1>
        <p class="brand__tagline">Family and Cosmetic Dentistry</p>
        <p class="brand__address">372 Hollisbrook Lane, Suite 118<br>Cary, NC 27634</p>
      </div>
    </div>
    <ul class="contact">
      <li class="contact__item">919-472-3081
        <svg class="contact__icon" viewBox="0 0 14 14"><circle cx="7" cy="7" r="7" fill="var(--teal)"/><path d="M3 6c0-2 8-2 8 0v1H9V6H5v1H3z M4.5 7.5h5l1 3h-7z" fill="#fff"/></svg></li>
      <li class="contact__item">919-472-3095
        <svg class="contact__icon" viewBox="0 0 14 14"><rect x="1" y="0.5" width="12" height="13" rx="3" fill="var(--teal)"/><rect x="4" y="4" width="6" height="1.4" fill="#fff"/><rect x="4" y="7" width="6" height="1.4" fill="#fff"/></svg></li>
      <li class="contact__item">www.lindqvistdds.example
        <svg class="contact__icon" viewBox="0 0 14 14"><circle cx="7" cy="7" r="6.5" fill="var(--teal)"/><path d="M.5 7h13M7 .5v13M7 .5c-3 3-3 10 0 13M7 .5c3 3 3 10 0 13" stroke="#fff" stroke-width=".7" fill="none"/></svg></li>
    </ul>
  </header>

  <div class="watermark" aria-hidden="true">Lindqvist</div>

  <footer class="letterhead__footer">
    <svg width="600" height="100" viewBox="0 0 600 100" aria-hidden="true">
      <path d="M0 100 C60 30 200 10 330 20 C450 30 520 25 600 18 L600 100 Z" fill="var(--wave-light)"/>
      <path d="M0 100 C70 40 210 22 330 30 C450 38 520 40 600 35 L600 100 Z" fill="var(--teal)"/>
    </svg>
    <p class="footer__motto">Precision Dentistry with a Personal Touch</p>
  </footer>
</main>
</body>
</html>
```